Perfume Oil manufacturing and distribution company needs an emotion inspiring Wordpress Design

Must be Wordpress Design
Beautiful website needed for a company that manufactures and distributes scents that fragrance products from fine fragrances to personal care and household products. Please refer to attached file (namely "brief" for detailed explanation of our company, product and design requirements)

Website must be beautiful, and not too cluttered.

Must be coded for use in WordPress after design phase

remember not to flood website with pictures of perfumes and perfume bottles, this website is meant to inspire emotion...looking at the big fragrance brands (Valdoret and Morvaleth) one will not see pictures of perfume bottles etc. The site is all about emotion and smell and the senses.
Keep this in mind when submitting designs.

The site must captivate and inspire emotion with beautiful visuals.

the website must be about how one feels when surrounded by a beautiful smell, how one feels confident wearing a good scent. how freshly baked break reminds you of your grandmas house, or how a scent can remind of a seductive encounter, or a memory of fun times with friends out on the town, or as simple as the smell of a good cup of coffee or a rose to inspire a new days happenings.

all this emotion and feeling must be tied into the fact that Aroma Nest makes these moments through great smells. Which we supply to manufacturers of these great end products. whether it is a fine fragrance, a lotion, a car fragrance or a home spray. We scent the world around us.

try not to look too much at our existing website as this is outdated and the company has changed much since then, refer to this and the attached brief

Target Market(s)

small to medium businesses who manufacture products that need to be fragranced. whether these products be prestigious fine fragrances, daily personal care products or home care products, we make the fragrances that make these products beautiful.

Industry/Entity Type

Perfume

Coding

Coded - Design and coding required

Number of Pages Required

5+ page

Font styles to use
Serif
Sans Serif

Colors

Designer to choose colors to be used in the design.

Requirements
Must have
• must have full page header that captivates audience and inspires emotion (through a video or powerful imagery)
• Smell is a powerful emotion trigger and since a computer screen can not produce smell we will need to engage emotion through beautiful imagery and or video and beautiful design on the website. (refer to attached "brief" for more details)
• Must be coded for use in WordPress ONLY after design phase
• site must work well and look great on mobile since most of our audience use mobile to access our site.
Should not have
• too many pictures of perfume packaging and actual products, looking at the big fragrance manufacturers (Valdoret, Morvaleth, KTB) one will not see pictures of perfume bottles and packaging. This is very important as the website is more to inspire emotion and give a sense of how fragrance and perfume makes one feel.
• The site must captivate and inspire emotion with beautiful visuals.

```html
<!DOCTYPE html>
<html lang="en">
<head>
<meta charset="utf-8">
<title>Aroma Nest – Master Perfumers</title>
<link rel="stylesheet" href="https://fonts.googleapis.com/css2?family=Lato:wght@300;400;700&display=swap">
<style>
  :root {
    --navy-deep: #0b1a2c;
    --navy: #13263b;
    --footer: #112338;
    --footer-line: #22384f;
    --hero-top: #0d2035;
    --hero-mid: #1a3a5c;
    --petal: #5f9fd6;
    --brand-blue: #3a9ad9;
    --white: #ffffff;
    --soft: #d7dfe8;
    --muted: #8a99a8;
    --panel-left: #5d6b7a;
    --panel-right: #4f5d6d;
    --btn-blue: #2e9fdc;
    --card: #c8ced4;
  }
  * { box-sizing: border-box; margin: 0; padding: 0; }
  html, body { width: 1124px; height: 1200px; overflow: hidden; }
  body { position: relative; font-family: "Lato", sans-serif; color: var(--white); background: var(--navy-deep); }

  .hero { position: absolute; left: 0; top: 0; width: 1124px; height: 540px; overflow: hidden; }
  .hero-visual {
    position: absolute; inset: 0;
    background:
      radial-gradient(ellipse 300px 280px at 760px 250px, rgba(95,159,214,.55), transparent 70%),
      radial-gradient(ellipse 420px 360px at 800px 180px, rgba(40,90,140,.5), transparent 75%),
      linear-gradient(180deg, var(--hero-top) 0%, var(--hero-mid) 45%, var(--navy-deep) 100%);
  }
  .brand { position: absolute; left: 420px; top: 18px; display: flex; align-items: center; gap: 12px; }
  .brand-dot { width: 58px; height: 58px; border-radius: 50%; background: var(--brand-blue); }
  .brand-name { font-size: 40px; font-weight: 700; color: var(--brand-blue); }
  .menu-toggle { position: absolute; right: 10px; top: 12px; }
  .hero-title {
    position: absolute; left: 0; top: 232px; width: 1124px; text-align: center;
    font-weight: 300; font-size: 51px; line-height: 50px;
  }
  .hero-button {
    position: absolute; left: 498px; top: 393px; width: 127px; height: 41px;
    border: 2px solid var(--white); border-radius: 3px;
    font-size: 16px; line-height: 37px; text-align: center;
  }

  .intro { position: absolute; left: 0; top: 540px; width: 1124px; height: 375px; }
  .intro-visual { position: absolute; top: 0; height: 375px; }
  .intro-visual.lab { left: 0; width: 561px; background: linear-gradient(135deg, #6c7a89, var(--panel-left) 50%, #3f4c5a); }
  .intro-visual.formula { left: 563px; width: 561px; background: linear-gradient(160deg, #3e4b5a, var(--panel-right) 55%, #6b7886); }
  .intro-card {
    position: absolute; top: 49px; width: 488px; height: 277px;
    border: 2px solid var(--white); border-radius: 3px; text-align: center; padding: 0 27px;
  }
  .intro-card.welcome { left: 36px; }
  .intro-card.products { left: 602px; }
  .intro-card h2 { font-weight: 300; font-size: 36px; margin-top: 10px; line-height: 44px; }
  .intro-card p { font-size: 14.5px; line-height: 26.5px; margin-top: 16px; }
  .intro-card .know-more {
    display: inline-block; margin-top: 19px; font-size: 15px; padding-bottom: 3px;
    border-bottom: 2px solid var(--white);
  }

  .site-footer { position: absolute; left: 0; top: 915px; width: 1124px; height: 285px; background: var(--footer); }
  .footer-col { position: absolute; top: 33px; }
  .footer-col h3 { font-size: 15px; font-weight: 400; margin-bottom: 14px; }
  .footer-col ul { list-style: none; }
  .footer-col li { font-size: 13px; line-height: 19.5px; }
  .contact { left: 25px; }
  .contact li { display: flex; gap: 10px; margin-bottom: 4.5px; }
  .contact li svg { flex: none; margin-top: 3px; }
  .contact li.address { margin-top: 10px; }
  .links li { position: relative; padding-left: 14px; }
  .links li::before {
    content: ""; position: absolute; left: 2px; top: 6px;
    border-left: 5px solid var(--brand-blue); border-top: 4px solid transparent; border-bottom: 4px solid transparent;
  }
  .services { left: 298px; width: 150px; }
  .categories { left: 454px; }
  .subscribe { left: 571px; width: 260px; }
  .subscribe p { font-size: 13px; line-height: 19px; }
  .subscribe-form { display: flex; margin-top: 12px; }
  .subscribe-form .field { width: 178px; height: 29px; background: var(--white); color: var(--muted); font-size: 11px; line-height: 29px; padding-left: 8px; }
  .subscribe-form .submit { width: 76px; height: 29px; background: var(--btn-blue); font-size: 12px; font-weight: 700; text-align: center; line-height: 29px; }
  .payment-label { font-size: 13px; margin-top: 10px; }
  .payment-methods { display: flex; gap: 8px; margin-top: 8px; }
  .payment-methods span { width: 35px; height: 21px; background: var(--card); border-radius: 2px; }

  .social-box { position: absolute; left: 846px; top: 37px; width: 254px; height: 196px; background: var(--white); border: 1px solid #dfe3e8; }
  .social-visual { height: 125px; background: linear-gradient(120deg, #5d6a72, #9aa39a 50%, #6d7a78); position: relative; }
  .social-head { position: absolute; left: 6px; top: 6px; display: flex; gap: 6px; }
  .social-head .mark { width: 30px; height: 30px; background: var(--white); }
  .social-head b { font-size: 13px; display: block; }
  .social-head small { font-size: 10px; }
  .social-like { position: absolute; left: 6px; top: 100px; width: 56px; height: 16px; background: var(--white); border-radius: 2px; }
  .social-friends { padding: 12px 14px; color: #4b4f56; font-size: 8.5px; }
  .friend-row { display: flex; gap: 3px; margin-top: 4px; }
  .friend-row span { width: 19px; height: 19px; background: #b7bec6; }

  .footer-rule { position: absolute; left: 0; top: 239px; width: 1124px; height: 1px; background: var(--footer-line); }
  .copyright { position: absolute; left: 0; top: 256px; width: 1124px; text-align: center; font-size: 13px; color: var(--muted); }
</style>
</head>
<body>
  <header class="hero">
    <div class="hero-visual" role="img" aria-label="Blue-toned close-up of a delicate flower cluster against a dark navy background"></div>
    <div class="brand"><span class="brand-dot"></span><span class="brand-name">Aroma Nest</span></div>
    <svg class="menu-toggle" width="22" height="18" viewBox="0 0 22 18" aria-label="Menu">
      <rect y="1" width="22" height="3" fill="#fff"/><rect y="7.5" width="22" height="3" fill="#fff"/><rect y="14" width="22" height="3" fill="#fff"/>
    </svg>
    <h1 class="hero-title">We create, manufacture and sell fragrance oils<br>that brings magic into our daily lives</h1>
    <div class="hero-button">Know more</div>
  </header>

  <section class="intro">
    <div class="intro-visual lab" role="img" aria-label="Muted laboratory scene with perfumery glassware"></div>
    <div class="intro-visual formula" role="img" aria-label="Glass bottles over faint chemical formula sketches"></div>
    <article class="intro-card welcome">
      <h2>Welcome to Aroma Nest</h2>
      <p>Aroma Nest is passionate about fragrances, we sell perfume oil compounds to manufacturers who then use this perfume oil in their finished products. These perfume oils are used in our customer end products such as fine fragrances, every day personal care products like lotions, shower gels, etc. as well as home and car care products and fragrances.</p>
      <span class="know-more">Know More</span>
    </article>
    <article class="intro-card products">
      <h2>Products</h2>
      <p>Aroma Nest is passionate about fragrances, we sell perfume oil compounds to manufacturers who then use this perfume oil in their finished products. These perfume oils are used in our customer end products such as fine fragrances, every day personal care products like lotions, shower gels, etc. as well as home and car care products and fragrances.</p>
      <span class="know-more">Know More</span>
    </article>
  </section>

  <footer class="site-footer">
    <div class="footer-col contact">
      <h3>Contact</h3>
      <ul>
        <li><svg width="12" height="10" viewBox="0 0 12 10"><rect x="0" y="1" width="12" height="8" fill="#3a9ad9"/><path d="M0 1 L6 6 L12 1" stroke="#112338" fill="none"/></svg>hello@aromanest.co.za</li>
        <li><svg width="12" height="12" viewBox="0 0 12 12"><path d="M2 1 L4.5 1 L5.5 4 L4 5 Q5 7.5 7 8 L8 6.5 L11 7.5 L11 10 Q5 11 1 3 Z" fill="#3a9ad9"/></svg>(+27)010 555 0142</li>
        <li><svg width="12" height="12" viewBox="0 0 12 12"><circle cx="6" cy="6" r="6" fill="#3fbf5f"/></svg>(+27) 074 555 0198</li>
        <li class="address"><svg width="12" height="12" viewBox="0 0 12 12"><path d="M6 0 A4 4 0 0 1 10 4 Q10 7 6 12 Q2 7 2 4 A4 4 0 0 1 6 0 Z" fill="#3a9ad9"/><circle cx="6" cy="4" r="1.5" fill="#112338"/></svg><span>14 Marlow Road, Eastbrook Dr, Lindvale,<br>Harrowfield,<br>Johannesburg – South Africa</span></li>
      </ul>
    </div>
    <div class="footer-col links services">
      <h3>Services</h3>
      <ul>
        <li>Fragrance Matching</li><li>FMCG fragrances</li><li>Product Formulation Advice</li><li>Fine Fragrances</li><li>Product Bases</li><li>Q&amp;C</li>
      </ul>
    </div>
    <div class="footer-col links categories">
      <h3>Categories</h3>
      <ul>
        <li>Home</li><li>About</li><li>Services</li><li>Products</li><li>Blog</li><li>Contact</li><li>Training</li><li>Career</li>
      </ul>
    </div>
    <div class="footer-col subscribe">
      <h3>Subscribe</h3>
      <p>Subscribe to our mailing list to get the update to your mail</p>
      <div class="subscribe-form"><span class="field">Enter your mail...</span><span class="submit">SUBMIT</span></div>
      <p class="payment-label">Accept payment</p>
      <div class="payment-methods"><span></span><span></span><span></span><span></span></div>
    </div>
    <div class="social-box">
      <div class="social-visual" role="img" aria-label="Small glass bottles of fragrance oil">
        <div class="social-head"><span class="mark"></span><div><b>Aroma Nest</b><small>785 likes</small></div></div>
        <span class="social-like"></span>
      </div>
      <div class="social-friends">Be the first of your friends to like this
        <div class="friend-row"><span></span><span></span><span></span><span></span><span></span><span></span><span></span><span></span><span></span></div>
      </div>
    </div>
    <div class="footer-rule"></div>
    <p class="copyright">© 2018 aromanest. All Rights Reserved</p>
  </footer>
</body>
</html>
```